house selling company website

i need a website that is to get customers to let us sell their house within 30 days with no sales fees based in the uk. iv uploaded a design i like for the website i own i want a copy of this but for the different logo ect need the house buying logo i own to be changed to house selling company
it needs to be able to flash up to sell your house today contact box to collect their details such as property type, address, number of bedrooms, (estate agents valuation) , best price you can accept after they have seen the main section banner with advertising why use us.
the three reasons in the banner to use us needs to be
1: We will sell your house in 30 days and ensure we take a buyers fee for our service from the buyer meaning your buyer is secured unlike with most estate agents
2: We do not charge you any fees at all! our small fee is charged to the buyer
3: A huge network of investors and private buyers connecting many estate agents, auction houses, investors, and private buyers to ensure a fast sale.

```html
<!DOCTYPE html>
<html lang="en">
<head>
<meta charset="utf-8">
<title>Harbourline Homes – Sell your house today</title>
<link href="https://fonts.googleapis.com/css2?family=Poppins:wght@400;500;600&display=swap" rel="stylesheet">
<style>
  :root {
    --blue: #2a9fd8;
    --blue-panel: rgba(44, 160, 220, 0.88);
    --green: #3cb44a;
    --green-panel: #49bb52;
    --login: #1f95d6;
    --ink: #111111;
    --white: #ffffff;
    --card: #fbfbfe;
    --footer: #2b98d7;
    --night-top: #0b0d2e;
    --night-bottom: #3a1aa0;
  }
  * { box-sizing: border-box; margin: 0; padding: 0; }
  html, body { width: 840px; height: 1200px; overflow: hidden; }
  body { font-family: "Poppins", sans-serif; position: relative; background: var(--night-top); color: var(--ink); }

  .hero-photo {
    position: absolute; left: 0; top: 0; width: 840px; height: 480px;
    background: linear-gradient(180deg, #3d4f8c 0%, #8a8fc0 22%, #c9c6dc 40%, #4f83b8 55%, #c9682f 68%, #2f6fb0 78%, #d5d4e2 100%);
  }
  .night-photo {
    position: absolute; left: 0; top: 480px; width: 840px; height: 491px;
    background: linear-gradient(180deg, var(--night-top) 0%, #1a1560 40%, var(--night-bottom) 75%, #7a2fb8 100%);
  }

  .site-header { position: absolute; left: 58px; right: 58px; top: 18px; height: 42px; display: flex; align-items: center; justify-content: space-between; }
  .brand { display: flex; align-items: center; gap: 10px; color: var(--white); font-size: 24px; font-weight: 400; letter-spacing: -0.3px; }
  .brand-mark { width: 26px; height: 26px; background: var(--white); border-radius: 4px; }
  .auth { display: flex; gap: 11px; }
  .auth a { display: flex; align-items: center; gap: 5px; height: 26px; padding: 0 12px; border-radius: 4px; color: var(--white); font-size: 10px; text-decoration: none; }
  .auth .login { background: var(--login); border-top-right-radius: 14px; }
  .auth .register { background: var(--green); }

  .headline { position: absolute; left: 0; width: 840px; top: 124px; text-align: center; font-size: 25px; font-weight: 500; color: var(--blue); }
  .headline strong { color: var(--green); font-weight: 600; }

  .valuation-form { position: absolute; left: 117px; top: 182px; width: 606px; height: 117px; }
  .valuation-form .panel-blue { position: absolute; inset: 0; background: var(--blue-panel); border-radius: 4px; }
  .valuation-form svg.panel-green { position: absolute; left: 0; top: 0; }
  .field { position: absolute; top: 26px; }
  .field label { display: block; color: var(--white); font-size: 8px; margin-bottom: 6px; }
  .select { height: 25px; background: var(--white); border-radius: 2px; display: flex; align-items: center; justify-content: space-between; padding: 0 10px; font-size: 8px; color: #333; }
  .select svg { width: 8px; height: 8px; }
  .form-note { position: absolute; left: 26px; top: 84px; color: var(--white); font-size: 12px; }
  .search-btn { position: absolute; left: 500px; top: 47px; width: 80px; height: 26px; background: var(--white); border-radius: 13px 13px 4px 13px; color: var(--green); font-size: 9.5px; display: flex; align-items: center; justify-content: center; }

  .reason { position: absolute; left: 58px; width: 724px; height: 114px; background: var(--card); border-radius: 5px; text-align: center; display: flex; flex-direction: column; justify-content: center; }
  .reason h2 { color: var(--green); font-weight: 500; font-size: 19.5px; line-height: 1.2; }
  .reason p { font-size: 12px; line-height: 22px; color: var(--ink); }
  .reason-1 { top: 424px; }
  .reason-2 { top: 570px; background: var(--white); }
  .reason-3 { top: 716px; }

  .site-footer { position: absolute; left: 0; top: 971px; width: 840px; height: 229px; background: var(--footer); color: var(--white); }
  .footer-brand { position: absolute; left: 58px; top: 94px; font-size: 20px; font-weight: 400; }
  .footer-col { position: absolute; top: 44px; font-size: 10px; }
  .footer-col h3 { font-weight: 400; font-size: 10px; margin-bottom: 17px; }
  .footer-col li { list-style: none; margin-bottom: 17px; }
  .col-product { left: 346px; }
  .col-explore { left: 562px; }
  .col-company { left: 717px; }
  .footer-legal { position: absolute; left: 346px; top: 166px; font-size: 10px; display: flex; gap: 15px; }
  .social { position: absolute; left: 718px; top: 166px; display: flex; gap: 15px; }
  .social span { width: 11px; height: 11px; background: var(--white); border-radius: 2px; display: block; }
</style>
</head>
<body>
  <div class="hero-photo" role="img" aria-label="Colourful waterfront houses reflected in calm water under a purple evening sky"></div>
  <div class="night-photo" role="img" aria-label="Neon city skyline at night under a starry sky"></div>

  <header class="site-header">
    <div class="brand"><span class="brand-mark"></span>Harbourline Homes</div>
    <nav class="auth">
      <a class="login" href="#">
        <svg width="9" height="10" viewBox="0 0 9 10" fill="none" stroke="#fff" stroke-width="1"><rect x="3" y="0.5" width="5.5" height="9" rx="1"/><path d="M0 5h5M3.5 3.5 5 5 3.5 6.5"/></svg>
        Login</a>
      <a class="register" href="#">
        <svg width="14" height="10" viewBox="0 0 14 10" fill="none" stroke="#fff" stroke-width="1.1"><circle cx="8.5" cy="3" r="2.3"/><path d="M4.5 9.5c0-2.2 1.8-3.5 4-3.5s4 1.3 4 3.5M0.5 4h4M2.5 2v4"/></svg>
        Register</a>
    </nav>
  </header>

  <h1 class="headline">Flash up to <strong>sell</strong> your house today</h1>

  <form class="valuation-form">
    <div class="panel-blue"></div>
    <svg class="panel-green" width="606" height="117" viewBox="0 0 606 117"><path d="M496 0H602a4 4 0 0 1 4 4V113a4 4 0 0 1-4 4H457Z" fill="var(--green-panel)"/></svg>
    <div class="field" style="left:26px;width:144px"><label>Property Type</label><div class="select">Residence or Commarcial<svg viewBox="0 0 8 8"><path d="M1 2.5 4 5.5 7 2.5" stroke="#222" fill="none" stroke-width="1.2"/></svg></div></div>
    <div class="field" style="left:188px;width:145px"><label>Address</label><div class="select">Type area/ Postal<svg viewBox="0 0 8 8"><path d="M1 2.5 4 5.5 7 2.5" stroke="#222" fill="none" stroke-width="1.2"/></svg></div></div>
    <div class="field" style="left:351px;width:88px"><label>Number of Bedrooms</label><div class="select">3<svg viewBox="0 0 8 8"><path d="M1 2.5 4 5.5 7 2.5" stroke="#222" fill="none" stroke-width="1.2"/></svg></div></div>
    <p class="form-note">Estate agents valuation</p>
    <div class="search-btn">Search</div>
  </form>

  <section class="reason reason-1">
    <h2>We will sell your house in 30 days</h2>
    <p>and ensure we take a buyers fee for our service from the buyer meaning<br>your buyer is secured unlike with most estate agents</p>
  </section>
  <section class="reason reason-2">
    <h2>We do not charge you any fees at all!</h2>
    <p>Our small fee is charged to the buyer</p>
  </section>
  <section class="reason reason-3">
    <h2>A huge network of investors and private buyers</h2>
    <p>connecting many estate agents, auction houses, investors, and private buyers to ensure a fast sale.</p>
  </section>

  <footer class="site-footer">
    <div class="footer-brand">Harbourline Homes</div>
    <div class="footer-col col-product"><h3>Product</h3><ul><li>Features</li><li>Pricing</li><li>Book a demo</li></ul></div>
    <div class="footer-col col-explore"><h3>Explore</h3><ul><li>Events</li><li>Blog</li></ul></div>
    <div class="footer-col col-company"><h3>Company</h3><ul><li>About us</li><li>Contact us</li></ul></div>
    <div class="footer-legal"><span>© 2023 Welcome. All right reserved.</span><span>Privacy Policy</span><span>Terms of Service</span></div>
    <div class="social"><span></span><span></span><span></span></div>
  </footer>
</body>
</html>
```